Webdesign für Konfigurator für individuelle Nahrungsergänzungsmittel
Zielgruppe
Die Sternperle (sternperle.de) ist Deutschlands erster Konfigurator für individuelle Nahrungsergänzungsmittel.
Wir stellen jedes Produkt von Hand her und fertigen ausschließlich in unserer Manufaktur in Halvenbrück. Jedes hergestellte Produkt ist individualisiert und trägt den Namen des Käufers.
Unsere Kunden/Kundinnen (ab jetzt ohne Gendern weiter, das wird sonst so sperrig) können sich aus über 180 Rohstoffen bedienen, diese frei kombinieren und von uns in eine Kapsel pressen lassen. Nicht nur die Inhaltsstoffe, auch die Farbe der Kapseln und auch unsere nachhaltige Verpackung (aus Papier und Kork) kann individuell gestaltet werden. Unsere Kunden sind Endkunden, Therapeuten und Händler.
*Wer sind unsere Kunden:
1.) Endkunden mit bekannten Problemen oder dem Wunsch, sich und seinem Körper etwas Gutes zu tun. ('Ich möchte meine Haut und mein Immunsystem unterstützen.')
2.) Endkunden, welche bereits ein oder mehrere Nahrungsergänzungen einnehmen und diese Einnahme vereinfachen wollen ('Nun alles in einer Kapsel')
3.) Endkunden, welche direkte Empfehlungen erhalten haben ('Nimm dies und das.')
4.) Ärzte, Heilpraktiker, Mykotherapeuten, Physiotherapeuten, Ernährungsberater, andere Heilberufe: wir bieten ein spannendes Partnerprogramm, welches dem Therapeuten erlaubt, Nahrungsergänzungen direkt für die Patienten zu konfigurieren. Der Fachmann wählt also die passenden Inhaltsstoffe aus unserem Portfolio aus. Die Dose trägt das Logo, den Namen und die Farbe der jeweiligen Praxis (wird mit dem Kundenkonto verknüpft). Der Patient bekommt eine Vorkasse-Rechnung vom Therapeuten mit und zahlt direkt an die Sternperle, welche das Paket nach Geldeingang direkt an den Patienten versendet. Der Therapeut profitiert durch sein Corporate Design wie auch durch eine Provision.
5.) Händler. Als Manufaktur bieten wir Kleinunternehmern die Möglichkeit, eigene Produkte für den Weiterverkauf herzustellen. Anders als große Loh..
Aufgabenstellung
Logo und CI kann dem bisherigen Design entnommen werden.
Die 'Löffel-Illustration' muss in Grundzügen übernommen werden, kann aber durchaus verändert werden.
Unsere Plattform ist Shopware 6.
Die verwendete Schriftarten sind Bitter und Calibri - dies ist aber nicht verpflichtend.

```html
<!DOCTYPE html>
<html lang="de">
<head>
<meta charset="utf-8">
<title>Sternperle – Webdesign Ansichten</title>
<link href="https://fonts.googleapis.com/css2?family=Open+Sans:wght@400&family=Signika:wght@400;500&display=swap" rel="stylesheet">
<style>
:root{
  --teal:#4fa79b;
  --teal-dark:#3f9386;
  --mint:#e5f1ed;
  --red:#e0424f;
  --ink:#2b2b2b;
  --muted:#555;
  --link:#2a3fd6;
  --paper:#ffffff;
  --green-a:#5d7a3a;
  --green-b:#9fb572;
  --orange-a:#c9731a;
  --orange-b:#f0a92e;
}
*{box-sizing:border-box;margin:0;padding:0}
html,body{width:1200px;height:2400px;overflow:hidden;background:var(--paper)}
body{position:relative;font-family:"Signika",sans-serif;color:var(--ink)}
.sheet-title{position:absolute;left:0;width:1200px;text-align:center;font-family:"Open Sans",sans-serif;font-weight:400;font-size:31px;line-height:36px;color:#111}
.screen{position:absolute;background:var(--paper);overflow:hidden;border:1px solid #ddd}
.desktop{width:724px}
.phone{width:206px}

/* header */
.site-header{background:var(--mint);display:flex;align-items:center;position:relative}
.desktop .site-header{height:66px;padding:0 30px}
.phone .site-header{height:42px;padding:0 8px}
.brand{display:flex;align-items:center;gap:6px}
.brand-dot{border-radius:50%;background:var(--red);flex:none}
.desktop .brand-dot{width:14px;height:14px}
.phone .brand-dot{width:9px;height:9px}
.brand-name{font-weight:500;color:var(--red)}
.desktop .brand-name{font-size:17px}
.phone .brand-name{font-size:11px}
.brand-claim{color:var(--ink);line-height:1.3}
.desktop .brand-claim{font-size:6.5px;margin-left:4px}
.phone .brand-claim{font-size:6.5px;margin-left:4px}
.main-nav{display:flex;gap:32px;margin-left:auto;font-size:7.5px}
.main-nav span{padding:3px 2px}
.main-nav .active{border-bottom:1.5px solid var(--teal);border-radius:0 0 4px 4px}
.burger{margin-left:auto;width:16px;height:11px;display:flex;flex-direction:column;justify-content:space-between}
.burger i{display:block;height:2px;background:#222}

/* hero */
.hero{position:relative;display:flex;align-items:center;justify-content:center;border-bottom:3px solid var(--teal)}
.hero-image{position:absolute;inset:0}
.hero-green{background:linear-gradient(100deg,var(--green-a),var(--green-b) 35%,#6f8a45 60%,#b7c98e 80%,var(--green-a))}
.hero-orange{background:linear-gradient(100deg,#8a4a12,var(--orange-a) 25%,var(--orange-b) 50%,#d9861f 75%,#7a3f10)}
.desktop .hero{height:88px}
.phone .hero{height:100px}
.pill{position:relative;background:var(--paper);border:2px solid var(--teal);border-radius:999px;text-align:center;color:var(--ink)}
.desktop .hero .pill{font-size:15px;padding:6px 14px}
.phone .hero .pill{font-size:14px;line-height:19px;padding:5px 26px;width:186px}

.crumbs{font-size:7px;display:flex;align-items:center;gap:6px}
.desktop .crumbs{height:28px;padding:0 13px}
.phone .crumbs{height:28px;padding:0 22px}
.crumbs a{color:var(--link);text-decoration:underline}

.band{background:var(--teal);display:flex;align-items:center;justify-content:center}
.desktop .band{height:44px}
.phone .band{height:56px;padding:0 6px}
.band .pill{border-color:var(--paper);font-size:10px;padding:5px 10px}
.phone .band .pill{font-size:9.5px;line-height:13px;padding:5px 14px;width:194px}

.intro{text-align:center;font-size:8px}
.desktop .intro{padding:30px 0 30px}
.phone .intro{padding:26px 6px 24px;font-size:9px;line-height:14px}

.cards{display:flex;justify-content:center;flex-wrap:wrap;gap:24px}
.card{border:1.5px solid var(--teal);border-radius:4px;background:var(--paper)}
.desktop .card{width:240px;padding:18px 12px 14px}
.phone .card{width:164px;padding:22px 10px 12px}
.card-head{display:flex;align-items:center;gap:6px;font-size:8.5px;margin-bottom:12px}
.phone .card-head{font-size:9.5px;justify-content:center;text-align:center}
.card ul,.card ol{padding-left:12px;font-size:6.5px;line-height:9px}
.phone .card ul{font-size:7.5px;line-height:11.5px}
.card li{margin-bottom:6px}
.icon{flex:none}

/* reasons */
.reasons{display:flex;justify-content:center;gap:24px;padding-top:32px}
.reason{width:180px;border:1px solid #cfe3de;border-radius:3px}
.phone .reason{width:178px;margin:0 auto}
.reason-head{background:var(--teal);display:flex;justify-content:center;align-items:center;height:36px}
.reason-head .pill{border:none;font-size:9.5px;padding:3px 12px}
.phone .reason-head .pill{font-size:10px;padding:3px 12px}
.reason ul{padding:18px 8px 12px 18px;font-size:6.5px;line-height:9px}
.phone .reason ul{padding:16px 10px 12px 18px;font-size:7.5px;line-height:11.5px}
.reason li{margin-bottom:5px}
</style>
</head>
<body>

<h1 class="sheet-title" style="top:78px">Ansicht der Therapeuten &amp; Händler Seite in 2 Scroll-Positionen auf<br>Desktop und Smartphone</h1>

<!-- Desktop, Scrollposition 1 -->
<section class="screen desktop" style="left:77px;top:262px;height:362px">
  <header class="site-header">
    <div class="brand"><span class="brand-dot"></span><span class="brand-name">Sternperle</span><span class="brand-claim">Konfiguriere deine<br>Nahrungsergänzung</span></div>
    <nav class="main-nav"><span>Sternperle-Konfigurator</span><span>Shop</span><span class="active">Für Therapeuten &amp; Händler</span><span>Warum Sternperle?</span><span>Über Uns</span></nav>
  </header>
  <div class="hero"><div class="hero-image hero-green" role="img" aria-label="Foto grüner Kapseln mit Pulver"></div><div class="pill">Für Therapeuten &amp; Händler</div></div>
  <div class="crumbs">Du bist hier: <a>Home</a> › <span>Für Therapeuten &amp; Händler</span></div>
  <div class="band"><div class="pill">Unser Partnerprogramm für Therapeuten</div></div>
  <p class="intro">Als Partner von Sternperle erhältst Du von uns:</p>
  <div class="cards">
    <div class="card"><div class="card-head"><svg class="icon" width="22" height="14" viewBox="0 0 22 14"><circle cx="5" cy="4" r="2.5" fill="#e0424f"/><circle cx="17" cy="4" r="2.5" fill="#e0424f"/><circle cx="11" cy="3" r="3" fill="#e0424f"/><path d="M0 13a5 4 0 0 1 10 0zM12 13a5 4 0 0 1 10 0z" fill="#4fa79b"/><path d="M5 14a6 6 0 0 1 12 0z" fill="#4fa79b"/></svg>Für Deine Klienten</div>
      <ul><li>Individuell auf sie zugeschnittene Nahrungsergänzung, von Dir in unserem Konfigurator zusammengestellt</li></ul></div>
    <div class="card"><div class="card-head"><svg class="icon" width="16" height="18" viewBox="0 0 16 18"><circle cx="8" cy="4" r="3.5" fill="#e0424f"/><rect x="1" y="10" width="14" height="8" rx="2" fill="none" stroke="#4fa79b" stroke-width="1.6"/><path d="M4 14h8" stroke="#4fa79b" stroke-width="1.6"/></svg>Für Dich und Deine Praxis</div>
      <ul><li>attraktive Vergütung</li></ul></div>
  </div>
</section>

<!-- Phone, Scrollposition 1 -->
<section class="screen phone" style="left:893px;top:402px;height:364px">
  <header class="site-header">
    <div class="brand"><span class="brand-dot"></span><span class="brand-name">Sternperle</span><span class="brand-claim">Konfiguriere deine<br>Nahrungsergänzung</span></div>
    <div class="burger"><i></i><i></i><i></i></div>
  </header>
  <div class="hero"><div class="hero-image hero-green" role="img" aria-label="Foto grüner Kapseln mit Pulver"></div><div class="pill">Für Therapeuten &amp; Händler</div></div>
  <div class="crumbs"><a>Home</a> › <span>Für Therapeuten &amp; Händler</span></div>
  <div class="band"><div class="pill">Unser Partnerprogramm für Therapeuten</div></div>
  <p class="intro">Als Partner von Sternperle erhältst Du von uns:</p>
  <div class="cards">
    <div class="card"><div class="card-head"><svg class="icon" width="22" height="14" viewBox="0 0 22 14"><circle cx="5" cy="4" r="2.5" fill="#e0424f"/><circle cx="17" cy="4" r="2.5" fill="#e0424f"/><circle cx="11" cy="3" r="3" fill="#e0424f"/><path d="M0 13a5 4 0 0 1 10 0zM12 13a5 4 0 0 1 10 0z" fill="#4fa79b"/><path d="M5 14a6 6 0 0 1 12 0z" fill="#4fa79b"/></svg>Für Deine Klienten</div></div>
  </div>
</section>

<!-- Desktop, Scrollposition 2 -->
<section class="screen desktop" style="left:73px;top:1018px;height:362px">
  <div class="band"><div class="pill">Unser Partnerprogramm für Therapeuten</div></div>
  <p class="intro">Als Partner von Sternperle erhältst Du von uns:</p>
  <div class="cards">
    <div class="card"><div class="card-head"><svg class="icon" width="22" height="14" viewBox="0 0 22 14"><circle cx="5" cy="4" r="2.5" fill="#e0424f"/><circle cx="17" cy="4" r="2.5" fill="#e0424f"/><circle cx="11" cy="3" r="3" fill="#e0424f"/><path d="M0 13a5 4 0 0 1 10 0zM12 13a5 4 0 0 1 10 0z" fill="#4fa79b"/><path d="M5 14a6 6 0 0 1 12 0z" fill="#4fa79b"/></svg>Für Deine Klienten</div>
      <ul><li>Individuell auf sie zugeschnittene Nahrungsergänzung, von Dir in unserem Konfigurator zusammengestellt</li><li>einen rabattierten Preis</li><li>Lieferung direkt nach Hause</li></ul></div>
    <div class="card"><div class="card-head"><svg class="icon" width="16" height="18" viewBox="0 0 16 18"><circle cx="8" cy="4" r="3.5" fill="#e0424f"/><rect x="1" y="10" width="14" height="8" rx="2" fill="none" stroke="#4fa79b" stroke-width="1.6"/><path d="M4 14h8" stroke="#4fa79b" stroke-width="1.6"/></svg>Für Dich und Deine Praxis</div>
      <ul><li>attraktive Vergütung</li><li>Deine Corporate-Identity (Name der Praxis, Logo, Farbe) auf den Etiketten der Sternperle-Dosen für Deine Klienten</li><li>einen Rezeptblock</li></ul></div>
    <div class="card"><div class="card-head"><svg class="icon" width="18" height="16" viewBox="0 0 18 16"><path d="M9 9V3M9 5c-3-3-5-1-5-1M9 5c3-3 5-1 5-1" stroke="#e0424f" stroke-width="1.6" fill="none"/><path d="M1 12c4 0 6-1 8 0h5c1 0 1 2 0 2H7" stroke="#4fa79b" stroke-width="1.6" fill="none"/></svg>So einfach geht's:</div>
      <ol><li>Du erstellst ein Kundenkonto bei Sternperle</li><li>Du konfigurierst die Nahrungsergänzung für Deinen Klienten.</li></ol></div>
  </div>
</section>

<!-- Phone, Scrollposition 2 -->
<section class="screen phone" style="left:905px;top:1150px;height:360px">
  <p class="intro" style="padding-top:10px">Als Partner von Sternperle erhältst Du von uns:</p>
  <div class="cards" style="gap:14px">
    <div class="card"><div class="card-head"><svg class="icon" width="22" height="14" viewBox="0 0 22 14"><circle cx="5" cy="4" r="2.5" fill="#e0424f"/><circle cx="17" cy="4" r="2.5" fill="#e0424f"/><circle cx="11" cy="3" r="3" fill="#e0424f"/><path d="M0 13a5 4 0 0 1 10 0zM12 13a5 4 0 0 1 10 0z" fill="#4fa79b"/><path d="M5 14a6 6 0 0 1 12 0z" fill="#4fa79b"/></svg>Für Deine Klienten</div>
      <ul><li>Individuell auf sie zugeschnittene Nahrungsergänzung, von Dir in unserem Konfigurator zusammengestellt</li><li>einen rabattierten Preis</li><li>Lieferung direkt nach Hause</li></ul></div>
    <div class="card"><div class="card-head"><svg class="icon" width="16" height="18" viewBox="0 0 16 18"><circle cx="8" cy="4" r="3.5" fill="#e0424f"/><rect x="1" y="10" width="14" height="8" rx="2" fill="none" stroke="#4fa79b" stroke-width="1.6"/><path d="M4 14h8" stroke="#4fa79b" stroke-width="1.6"/></svg>Für Dich und Deine Praxis</div>
      <ul><li>attraktive Vergütung</li><li>Deine Corporate-Identity (Name der Praxis, Logo, Farbe) auf den Etiketten der Sternperle-Dosen für Deine Klienten</li></ul></div>
  </div>
</section>

<h2 class="sheet-title" style="top:1680px">Ansicht der Warum-Sternperle-Seite:</h2>

<!-- Desktop, Warum-Seite -->
<section class="screen desktop" style="left:62px;top:1790px;height:358px">
  <header class="site-header">
    <div class="brand"><span class="brand-dot"></span><span class="brand-name">Sternperle</span><span class="brand-claim">Konfiguriere deine<br>Nahrungsergänzung</span></div>
    <nav class="main-nav"><span>Sternperle-Konfigurator</span><span>Shop</span><span>Für Therapeuten &amp; Händler</span><span class="active">Warum Sternperle?</span><span>Über Uns</span></nav>
  </header>
  <div class="hero"><div class="hero-image hero-orange" role="img" aria-label="Foto von Kurkumapulver auf Löffel und orangen Kapseln"></div><div class="pill">Warum Sternperle?</div></div>
  <div class="crumbs">Du bist hier: <a>Home</a> › <span>Warum Sternperle?</span></div>
  <div class="reasons">
    <div class="reason"><div class="reason-head"><div class="pill">Made in Germany</div></div>
      <ul><li>Unser Team fertigt nacheinander jede Bestellung in unserer Manufaktur in Halvenbrück.</li><li>Obwohl es bei erhöhtem Bestellaufkommen zu längeren Wartezeiten kommen kann, haben wir keinen der Produktionsschritte ausgelagert.</li></ul></div>
    <div class="reason"><div class="reason-head"><div class="pill">Höchste Qualität</div></div>
      <ul><li>Wir verwenden ausschließlich mehrfach geprüfte, hochwertige Rohstoffe von deutschen Großhändlern.</li><li>Bei uns kommen smarte Technik sowie innovative Wiege-, Kontroll- und OS-Systeme zum Einsatz.</li></ul></div>
    <div class="reason"><div class="reason-head"><div class="pill">So individuell wie Du</div></div>
      <ul><li>Dir stehen über 180 Inhaltsstoffe zur Verfügung.</li><li>Daraus ergeben sich mehr als 1.000.000.000.000.000 mögliche Kombinationen.</li><li>Du kannst Deine Sternperle genau an Deine Bedürfnisse anpassen.</li></ul></div>
  </div>
</section>

<!-- Phone, Warum-Seite -->
<section class="screen phone" style="left:888px;top:1932px;height:364px">
  <header class="site-header">
    <div class="brand"><span class="brand-dot"></span><span class="brand-name">Sternperle</span><span class="brand-claim">Konfiguriere deine<br>Nahrungsergänzung</span></div>
    <div class="burger"><i></i><i></i><i></i></div>
  </header>
  <div class="hero"><div class="hero-image hero-orange" role="img" aria-label="Foto von Kurkumapulver auf Löffel und orangen Kapseln"></div><div class="pill" style="width:176px;padding:5px 8px">Warum Sternperle?</div></div>
  <div class="crumbs"><a>Home</a> › <span>Warum Sternperle?</span></div>
  <div style="padding-top:20px">
    <div class="reason"><div class="reason-head"><div class="pill">Made in Germany</div></div>
      <ul><li>Unser Team fertigt nacheinander jede Bestellung in unserer Manufaktur in Halvenbrück.</li><li>Obwohl es bei erhöhtem Bestellaufkommen zu längeren Wartezeiten kommen kann, haben wir keinen der Produktionsschritte ausgelagert.</li></ul></div>
  </div>
</section>

</body>
</html>
```